Sidebar ad for rare disease patient registries

We have a product (ANCHOR) that allows patient advocacy foundations to promote our patient registries while maintaining their own branding. We need a sidebar ad and banner ad designed that we could provide to the advocacy organizations to post on their own websites. The advocacy groups get a unique URL from us and they promote this URL to their disease community. When a user clicks the link, we change the branding on our site to reflect the advocacy organization's branding.

Having the ability to have a quality graphical ad on their foundation webpages that entice their patient community to join our registries is be critical. Looking for something about 230 px wide by 500 px tall.

We would provide multiple different text messages on the ads, so need room to have a headline and maybe a short sentence and a button that users would push to 'ANCHOR' to join the patient registry.

Would like a stylized button with the word ANCHOR on it which would take the user to our registry. Possibly include the carebridgeway logo in the button / graphic somehow in a tasteful way. CareBridgeway operates the technology and registry program, but we don't want to overtly brand ourselves but would like to include our brand if possible. We can not get between the advocacy organizations and the patient community. This is very much about trust with the patient community and asking them to share detailed medical history. They will not be sharing their information with CareBridgeway, but rather the advocacy organization that will have this ad on their website.

Would eventually like a series of graphics that an advocacy organization could choose from.

Example tag lines:

Give future generations a precious gift: your medical information

Give the global patient community the gift of your participation

Help researchers to help patients: Participate in trials and studies

Help researchers help you: Join our patient registry

The more researchers know about patients, the sooner they can find answers

Joining the patient registry helps the global patient community

Make your medical information count! Join the [your disease] registry

Pharma can’t invest in research if they don’t know how many patients have [your disease]. Help us build our patient registry.

There’s power in numbers. Help us build our patient registry.

Why participate in the [your disease] registry? Raise the visibility of [your disease] and generate more research interest.

FYI, our logo can be found at http://www.carebridgeway-example.com/templates/ja_social/images/logo.png

Also, we would prefer images that reflect patients as opposed to healthcare professionals if possible and please mention the words Patient Registry in the text.

Target Market(s)

Disease foundations and patient advocacy organizations. For example:
http://www.renalhopefund-example.org
http://www.mybrainpressure-example.com/
http://www.tobiasstillgoing-example.org
http://www.familyeffortmw-example.org
http://www.musclewaveaction-example.org

Industry/Entity Type

Product

```html
<!DOCTYPE html>
<html lang="en">
<head>
<meta charset="utf-8">
<title>CareBridgeway Patient Registry Sidebar Ad</title>
<link rel="stylesheet" href="https://fonts.googleapis.com/css2?family=Roboto:wght@300;400&family=Kalam:wght@400&family=Josefin+Sans:wght@600&display=swap">
<style>
  :root {
    --stage-bg: #4a4f55;
    --ad-bg: #f2f3f4;
    --ad-border: #d6d8da;
    --brand-blue: #3a8fd9;
    --headline-blue: #2b95e8;
    --ink-dark: #3a3a3a;
    --illus-light: #eef1f4;
    --illus-mid: #c9d4de;
    --illus-deep: #a9b8c6;
    --white: #ffffff;
  }
  * { margin: 0; padding: 0; box-sizing: border-box; }
  html, body {
    width: 1200px;
    height: 900px;
    overflow: hidden;
    background: var(--stage-bg);
  }
  .stage { position: relative; width: 1200px; height: 900px; }
  .sidebar-ad {
    position: absolute;
    left: 427px;
    top: 75px;
    width: 345px;
    height: 750px;
    background: var(--ad-bg);
    border: 1px solid var(--ad-border);
    overflow: hidden;
  }
  .visually-hidden {
    position: absolute;
    width: 1px; height: 1px;
    overflow: hidden;
    clip: rect(0 0 0 0);
    white-space: nowrap;
  }
  .brand {
    position: absolute;
    left: 8px;
    top: 22px;
    display: flex;
    align-items: center;
    gap: 9px;
  }
  .brand-dot {
    width: 24px;
    height: 24px;
    border-radius: 50%;
    background: var(--brand-blue);
  }
  .brand-name {
    font-family: "Roboto", sans-serif;
    font-weight: 400;
    font-size: 25px;
    letter-spacing: 5px;
    color: var(--brand-blue);
    white-space: nowrap;
  }
  .header-swoosh {
    position: absolute;
    left: 0;
    top: 66px;
    width: 345px;
    height: 34px;
  }
  .hero-illustration {
    position: absolute;
    left: 8px;
    top: 84px;
    width: 322px;
    height: 322px;
    border-radius: 4px;
    background: linear-gradient(160deg, var(--illus-light) 0%, var(--illus-mid) 60%, var(--illus-deep) 100%);
  }
  .headline {
    position: absolute;
    left: 19px;
    top: 433px;
    width: 320px;
    font-family: "Roboto", sans-serif;
    font-weight: 300;
    font-size: 46px;
    line-height: 48px;
    color: var(--headline-blue);
  }
  .headline-line { display: block; white-space: nowrap; }
  .subline {
    position: absolute;
    left: 19px;
    top: 585px;
    font-family: "Kalam", cursive;
    font-size: 29px;
    line-height: 40px;
    color: var(--ink-dark);
    white-space: nowrap;
  }
  .cta-button {
    position: absolute;
    left: 38px;
    top: 652px;
    width: 260px;
    height: 64px;
    display: block;
    text-decoration: none;
  }
  .cta-button svg { position: absolute; inset: 0; }
  .cta-label {
    position: absolute;
    left: 72px;
    top: 19px;
    font-family: "Josefin Sans", sans-serif;
    font-weight: 600;
    font-size: 29px;
    line-height: 30px;
    letter-spacing: 1px;
    color: var(--white);
  }
</style>
</head>
<body>
<div class="stage">
  <aside class="sidebar-ad" aria-label="Join the Patient Registry">
    <div class="brand">
      <span class="brand-dot"></span>
      <span class="brand-name">CareBridgeway</span>
    </div>

    <svg class="header-swoosh" viewBox="0 0 345 34" aria-hidden="true">
      <defs>
        <linearGradient id="swoosh-green" x1="0" x2="1" y1="0" y2="0">
          <stop offset="0" stop-color="#5a9e2a"/>
          <stop offset="1" stop-color="#8cc63f"/>
        </linearGradient>
      </defs>
      <path d="M0 24 Q150 4 345 8 L345 15 Q150 12 0 32 Z" fill="url(#swoosh-green)"/>
    </svg>

    <div class="hero-illustration" role="img" aria-label="Patient Registry illustration: a medical record sheet with a blood pressure cuff, gauge and a glossy red heart"></div>

    <h1 class="headline">
      <span class="headline-line">Give future</span>
      <span class="headline-line">generations</span>
      <span class="headline-line">a precious gift</span>
    </h1>
    <p class="subline">your medical information</p>

    <a class="cta-button" href="#" aria-label="ANCHOR – join the Patient Registry">
      <svg viewBox="0 0 260 64" aria-hidden="true">
        <defs>
          <linearGradient id="button-green" x1="0" x2="0" y1="0" y2="1">
            <stop offset="0" stop-color="#9ad14a"/>
            <stop offset="1" stop-color="#5a9e2a"/>
          </linearGradient>
        </defs>
        <path d="M6 0 H232 L260 32 L232 64 H6 Q0 64 0 58 V6 Q0 0 6 0 Z" fill="url(#button-green)"/>
        <circle cx="34" cy="32" r="20" fill="#ffffff"/>
      </svg>
      <span class="cta-label">ANCHOR</span>
      <span class="visually-hidden">Join the Patient Registry</span>
    </a>
  </aside>
</div>
</body>
</html>
```